Design my New and Engaging Wix Website

We just recently started a new website for Harbor Lumen (www.harbor-lumen.example) and would like to have a custom design for it. The design should be engaging and modern. You can use our logo and design the website inspired by the style.

```html
<!DOCTYPE html>
<html lang="en">
<head>
<meta charset="utf-8">
<title>Harbor Lumen – Education Resources</title>
<link href="https://fonts.googleapis.com/css2?family=Montserrat:wght@400;500;600;700&family=Quicksand:wght@500;600&display=swap" rel="stylesheet">
<style>
:root{
  --blue:#0f8ee0;
  --blue-dark:#0a7cc6;
  --ink:#1b1b1b;
  --text:#3a3a3a;
  --muted:#f1f1f1;
  --white:#ffffff;
  --green:#5b8c32;
  --line:#d9d9d9;
}
*{box-sizing:border-box;margin:0;padding:0}
html,body{width:1200px;height:5089px;overflow:hidden}
body{position:relative;background:var(--white);font-family:"Montserrat",sans-serif;color:var(--text)}
.abs{position:absolute}
.heading{font-family:"Quicksand",sans-serif;font-weight:500;color:var(--blue);font-size:34px;line-height:1.1}
.heading-rule{position:absolute;height:2px;background:var(--blue)}
.body-copy{font-size:12.5px;line-height:24px;color:var(--text)}
.btn{position:absolute;background:var(--blue);color:var(--white);font-size:12px;font-weight:500;letter-spacing:.5px;text-align:center;border-radius:4px;box-shadow:-4px -4px 0 0 var(--white),-5px -5px 0 0 var(--blue)}
.photo{position:absolute}

/* header */
.site-header{position:absolute;left:0;top:0;width:1200px;height:88px;border-bottom:1px solid var(--line);background:var(--white)}
.brand{position:absolute;left:160px;top:22px;display:flex;align-items:center;gap:10px;font-size:26px;font-weight:500;color:var(--blue)}
.brand-dot{width:26px;height:26px;border-radius:50%;background:var(--blue)}
.nav a{position:absolute;top:40px;font-size:12px;color:var(--ink);text-decoration:none;letter-spacing:.3px}
.nav a.active{color:var(--blue)}
.call{position:absolute;left:940px;top:30px;font-size:12px;line-height:18px;color:var(--ink)}
.call b{color:var(--blue);font-weight:500;display:block}

/* hero */
.hero{position:absolute;left:0;top:88px;width:1200px;height:587px;background:linear-gradient(90deg,#f3f3f3 0%,#ececec 55%,#e4e6ea 100%)}
.hero-title{position:absolute;left:158px;top:200px;font-size:30px;font-weight:600;color:var(--ink);line-height:40px}
.hero-title span{display:block;color:var(--blue)}
.hero-sub{position:absolute;left:162px;top:290px;font-size:14px;color:var(--ink)}

/* cards */
.card{position:absolute;top:1388px;width:270px;height:437px;background:var(--white);border-radius:8px;box-shadow:0 3px 12px rgba(0,0,0,.08);overflow:hidden}
.card-photo{height:222px}
.card-icon{position:absolute;left:22px;top:245px}
.card-title{position:absolute;left:20px;top:306px;font-size:15px;font-weight:500;color:var(--ink);line-height:24px;letter-spacing:.3px}
.card-text{position:absolute;left:20px;top:362px;font-size:12px;line-height:22px;width:240px}

/* consortium */
.partner{position:absolute;top:2870px;width:431px;height:288px;background:var(--white);border-radius:8px;box-shadow:0 3px 12px rgba(0,0,0,.06);overflow:hidden}
.partner-photo{position:absolute;left:0;top:0;width:195px;height:288px}
.partner-name{position:absolute;left:217px;top:44px;font-size:15px;font-weight:500;color:var(--ink);line-height:24px;width:200px}
.partner-text{position:absolute;left:217px;font-size:12px;line-height:21px;width:200px}

/* blogs */
.blog{position:absolute;top:4215px;width:270px;height:110px}
.cal{position:absolute;left:0;top:0;width:60px;height:64px;border:4px solid var(--blue);border-top-width:12px;border-radius:6px;text-align:center;background:var(--white)}
.cal b{display:block;font-size:18px;font-weight:600;color:var(--ink);margin-top:4px}
.cal small{font-size:12px;color:var(--ink)}
.cal::before,.cal::after{content:"";position:absolute;top:-20px;width:5px;height:12px;background:var(--blue);border-radius:2px}
.cal::before{left:12px}.cal::after{right:12px}
.blog-title{position:absolute;left:96px;top:0;font-size:15px;font-weight:500;color:var(--ink);line-height:24px}
.blog-text{position:absolute;left:96px;top:54px;font-size:12px;line-height:22px;width:180px}
.blog-more{position:absolute;left:96px;top:104px;font-size:11px;font-weight:600;text-decoration:underline;color:var(--ink)}
.arrow{position:absolute;font-size:34px;color:var(--blue);font-weight:400}

/* footer */
.site-footer{position:absolute;left:0;top:4728px;width:1200px;height:361px;background:var(--blue)}
.footer-brand{position:absolute;left:0;width:1200px;top:72px;display:flex;justify-content:center;align-items:center;gap:14px;font-size:42px;font-weight:500;color:var(--white)}
.footer-brand i{width:34px;height:34px;border-radius:50%;background:var(--white)}
.footer-nav{position:absolute;left:0;width:1200px;top:186px;display:flex;justify-content:center;gap:26px;font-size:12px;color:#dff0fb}
.social{position:absolute;top:236px;width:34px;height:34px;border-radius:50%;border:2px solid var(--white)}
.copyright{position:absolute;left:0;width:1200px;top:308px;text-align:center;font-size:12px;color:#dff0fb}
</style>
</head>
<body>

<header class="site-header">
  <div class="brand"><span class="brand-dot"></span>Harbor Lumen</div>
  <nav class="nav">
    <a class="active" style="left:566px">HOME</a>
    <a style="left:642px">OUR PROJECT</a>
    <a style="left:775px">CONTACT US</a>
  </nav>
  <svg class="abs" style="left:896px;top:34px" width="26" height="26" viewBox="0 0 24 24" fill="none" stroke="#0f8ee0" stroke-width="1.6"><path d="M5 3h4l2 5-3 2a12 12 0 0 0 6 6l2-3 5 2v4a2 2 0 0 1-2 2A18 18 0 0 1 3 5a2 2 0 0 1 2-2z"/></svg>
  <div class="call"><b>CALL US</b>(555)-010-2040</div>
</header>

<section class="hero">
  <div class="photo" role="img" aria-label="Student wearing headphones working on a laptop in front of a faint globe" style="left:560px;top:0;width:640px;height:587px;background:linear-gradient(90deg,rgba(230,232,236,0) 0%,#dfe3e8 30%,#7fb4e6 65%,#d9c2a5 100%)"></div>
  <h1 class="hero-title">Qualitative and Accessible<span>Harbor Lumen Resources</span></h1>
  <p class="hero-sub">Our Mission and Contribution</p>
  <div class="btn" style="left:162px;top:342px;width:186px;height:40px;line-height:40px;box-shadow:-4px -4px 0 0 #ececec,-5px -5px 0 0 var(--blue)">CONTACT US TODAY</div>
</section>

<!-- about -->
<svg class="abs" style="left:166px;top:770px" width="408" height="350" fill="none" stroke="#0f8ee0" stroke-width="2" stroke-dasharray="22 10"><path d="M2 60V2h210M400 180v110a50 50 0 0 1-50 50H180"/></svg>
<div class="photo" role="img" aria-label="Three students smiling at a laptop together" style="left:182px;top:788px;width:370px;height:320px;border-radius:0 40px 0 40px;background:linear-gradient(135deg,#c9a98a,#8aa9c9 55%,#d8d0c6)"></div>
<div class="heading-rule" style="left:646px;top:798px;width:100px"></div>
<h2 class="heading abs" style="left:646px;top:808px">About Harbor Lumen</h2>
<p class="body-copy abs" style="left:646px;top:856px;width:400px">In an increasingly internationalized world, complex and manifold conflicts arise between individuals, groups, organizations, and states.<br>To find ways of dealing with these issues in a constructive and peaceful manner is a central challenge for modern societies. Harbor Lumen aims to empower communities affected by unresolved conflicts and strengthen their capacities to address them effectively.</p>
<div class="btn" style="left:650px;top:1082px;width:122px;height:38px;line-height:38px">READ MORE</div>

<!-- what we do -->
<div class="heading-rule" style="left:524px;top:1266px;width:152px"></div>
<h2 class="heading abs" style="left:0;width:1200px;text-align:center;top:1274px">What We Do</h2>
<p class="abs" style="left:0;width:1200px;text-align:center;top:1318px;font-size:12px;line-height:21px">Lorem ipsum dolor sit amet, consectetuer adipiscing elit, sed diam nonummy nibh<br>euismod tincidunt ut laoreet dolore magna aliquam erat volutpat.</p>

<article class="card" style="left:162px">
  <div class="card-photo" role="img" aria-label="Library shelves full of books" style="background:linear-gradient(180deg,#8a5a3a,#c49a6a 70%,#fff)"></div>
  <svg class="card-icon" width="48" height="48" fill="none" stroke="#0f8ee0" stroke-width="2"><circle cx="24" cy="24" r="20"/><path d="M14 30h20M16 18h16v12H16z"/></svg>
  <h3 class="card-title">DEVELOPING PEACE<br>EDUCATION CURRICULAR</h3>
  <p class="card-text">Modernizing and internationalizing higher education</p>
</article>
<article class="card" style="left:465px">
  <div class="card-photo" role="img" aria-label="Trainer speaking with a group of adults" style="background:linear-gradient(180deg,#6b6f74,#b9b3ac 70%,#fff)"></div>
  <svg class="card-icon" width="48" height="48" fill="none" stroke="#0f8ee0" stroke-width="2"><rect x="18" y="4" width="26" height="18"/><circle cx="14" cy="24" r="6"/><path d="M4 44v-6a10 10 0 0 1 20 0v6z"/></svg>
  <h3 class="card-title">TEACHING<br>AND TRAINING</h3>
  <p class="card-text">Utilizing the potential of hybrid learning</p>
</article>
<article class="card" style="left:768px">
  <div class="card-photo" role="img" aria-label="Presenter recording a video lesson" style="background:linear-gradient(180deg,#4c4a48,#a9a49c 70%,#fff)"></div>
  <svg class="card-icon" width="48" height="48" fill="none" stroke="#0f8ee0" stroke-width="2"><circle cx="14" cy="14" r="7"/><circle cx="34" cy="12" r="7"/><rect x="4" y="28" width="30" height="16"/></svg>
  <h3 class="card-title">PRODUCING PEACE<br>EDUCATION RESOURCES</h3>
  <p class="card-text">Providing engaging and high quality content</p>
</article>
<div class="btn" style="left:528px;top:1866px;width:148px;height:38px;line-height:38px">CONTACT US</div>

<!-- conflict triangle -->
<div class="heading-rule" style="left:162px;top:2152px;width:100px"></div>
<h2 class="heading abs" style="left:162px;top:2162px">Conflict Triangle</h2>
<p class="body-copy abs" style="left:162px;top:2222px;width:366px">Lorem ipsum dolor sit amet, consectetuer adipiscing elit, sed diam nonummy nibh euismod tincidunt ut laoreet dolore magna aliquam erat volutpat. Ut wisi enim ad minim veniam, quis nostrud exerci tation ullamcorper suscipit lobortis nisl ut aliquip ex ea commodo consequat. Duis autem vel eum iriure dolor in hendrerit in vulputate velit esse molestie consequat.</p>
<svg class="abs" style="left:606px;top:2010px" width="594" height="490" fill="none" stroke="#555" stroke-width="2" stroke-dasharray="22 10"><path d="M2 40v400a46 46 0 0 0 46 46h546"/></svg>
<div class="photo" role="img" aria-label="Animated diagram of people connected to a central dialogue circle" style="left:616px;top:2015px;width:584px;height:475px;border-radius:40px 0 0 40px;background:var(--green)"></div>
<svg class="abs" style="left:542px;top:2186px" width="136" height="136"><circle cx="68" cy="68" r="66" fill="#0f8ee0" opacity=".12"/><circle cx="68" cy="68" r="48" fill="#0f8ee0" opacity=".2"/><circle cx="68" cy="68" r="34" fill="#0f8ee0"/><path d="M60 52l24 16-24 16z" fill="#fff"/></svg>

<!-- consortium -->
<section class="abs" style="left:0;top:2607px;width:1200px;height:666px;background:var(--muted)"></section>
<div class="heading-rule" style="left:534px;top:2750px;width:150px"></div>
<h2 class="heading abs" style="left:0;width:1200px;text-align:center;top:2758px">PROJECT CONSORTIUM</h2>
<p class="abs" style="left:0;width:1200px;text-align:center;top:2822px;font-size:12px">Cross-Border Cooperation</p>
<article class="partner" style="left:162px">
  <div class="partner-photo" role="img" aria-label="Historic stone university building" style="background:linear-gradient(180deg,#9fbfe0,#8a7c6c 55%,#b5b0a6)"></div>
  <h3 class="partner-name">NORTHVALE STATE<br>UNIVERSITY</h3>
  <p class="partner-text" style="top:94px">Lorem ipsum dolor sit amet con sectetuer adipiscing elit, sed diam nonummy nibh euis mod tincidunt ut laoreet dol ore magna aliquam erat volutpat.</p>
</article>
<article class="partner" style="left:607px">
  <div class="partner-photo" role="img" aria-label="Yellow neoclassical academy building with columns" style="background:linear-gradient(180deg,#5f92d0,#d9c47a 55%,#9c9a8c)"></div>
  <h3 class="partner-name">EASTBROOK RIVERSIDE<br>ACADEMY</h3>
  <p class="partner-text" style="top:118px">Lorem ipsum dolor sit amet con sectetuer adipiscing elit, sed diam nonummy nibh euis mod tincidunt ut laoreet dol ore magna aliquam eratvol.</p>
</article>

<!-- donor -->
<div class="photo" role="img" aria-label="Modern office building with banners beside a street" style="left:0;top:3380px;width:590px;height:478px;border-radius:0 40px 0 0;background:linear-gradient(180deg,#dfe4e6,#9ea7a9 45%,#6f7a5e 75%,#55575a)"></div>
<svg class="abs" style="left:0;top:3378px" width="600" height="490" fill="none" stroke="#555" stroke-width="2" stroke-dasharray="22 10"><path d="M596 40v400a46 46 0 0 1-46 46H0"/></svg>
<div class="heading-rule" style="left:662px;top:3510px;width:100px"></div>
<h2 class="heading abs" style="left:660px;top:3518px">DONOR</h2>
<div class="abs" style="left:662px;top:3592px;width:64px;height:64px;border-radius:50%;background:#1f4f8f;color:#fff;font-size:16px;line-height:64px;text-align:center">AEF</div>
<p class="abs" style="left:746px;top:3610px;font-size:10px;line-height:14px;color:#1f4f8f">Academic Exchange Fund<br>International Study Partners</p>
<div class="arrow" style="left:1060px;top:3598px">&#8250;</div>
<p class="body-copy abs" style="left:662px;top:3676px;width:400px">Lorem ipsum dolor sit amet, consectetuer adipiscing elit, sed diam nonummy nibh euismod tincidunt ut laoreet dolore magna aliquam erat volutpat. Ut wisi enim ad minim veniam, quis nostrud exerci tation.</p>

<!-- blogs -->
<section class="abs" style="left:0;top:3972px;width:1200px;height:548px;background:var(--muted)"></section>
<div class="heading-rule" style="left:528px;top:4120px;width:150px"></div>
<h2 class="heading abs" style="left:0;width:1200px;text-align:center;top:4128px">LATEST BLOGS</h2>
<div class="arrow" style="left:122px;top:4240px">&#8249;</div>
<div class="arrow" style="left:1062px;top:4240px">&#8250;</div>
<article class="blog" style="left:162px"><div class="cal"><b>06th</b><small>Oct</small></div><h3 class="blog-title">Lorem Ipsum Dolor<br>Awectetuer</h3><p class="blog-text">Lorem ipsum dolor amet, consec ingrer elit diam</p><a class="blog-more">READ MORE</a></article>
<article class="blog" style="left:468px"><div class="cal"><b>26th</b><small>Nov</small></div><h3 class="blog-title">Lorem Ipsum Dolor<br>Awectetuer</h3><p class="blog-text">Lorem ipsum dolor amet, consec ingrer elit diam</p><a class="blog-more">READ MORE</a></article>
<article class="blog" style="left:775px"><div class="cal"><b>04th</b><small>Dec</small></div><h3 class="blog-title">Lorem Ipsum Dolor<br>Awectetuer</h3><p class="blog-text">Lorem ipsum dolor amet, consec ingrer elit diam</p><a class="blog-more">READ MORE</a></article>
<div class="btn" style="left:540px;top:4376px;width:122px;height:38px;line-height:38px;box-shadow:-4px -4px 0 0 var(--muted),-5px -5px 0 0 var(--blue)">VIEW ALL</div>

<!-- newsletter -->
<div class="heading-rule" style="left:204px;top:4610px;width:96px"></div>
<h2 class="heading abs" style="left:200px;top:4618px">Newsletter Signup</h2>
<div class="abs" style="left:520px;top:4596px;width:462px;height:44px;background:var(--white);box-shadow:0 2px 10px rgba(0,0,0,.1);border-radius:3px"></div>
<svg class="abs" style="left:538px;top:4612px" width="14" height="11" fill="none" stroke="#999" stroke-width="1.3"><rect x=".7" y=".7" width="12.6" height="9.6"/><path d="M1 1l6 5 6-5"/></svg>
<p class="abs" style="left:566px;top:4611px;font-size:12px;color:#999">Enter Your Email Address</p>
<div class="abs" style="left:858px;top:4600px;width:122px;height:36px;line-height:36px;background:var(--blue);color:#fff;font-size:12px;text-align:center;border-radius:3px">SUBSCRIBE</div>

<footer class="site-footer">
  <div class="footer-brand"><i></i>Harbor Lumen</div>
  <div class="footer-nav"><span style="color:#fff">HOME</span><span>OUR PROJECTS</span><span>CONTACT US</span><span>Call Us: (555) 010 2041</span><span>Email Us: hello@harbor-lumen.example</span></div>
  <span class="social" style="left:504px"></span>
  <span class="social" style="left:583px"></span>
  <span class="social" style="left:662px"></span>
  <p class="copyright">Copyright © 2021 Harbor Lumen. All Rights Reserved.</p>
</footer>

</body>
</html>
```